Shopping centre customer engagement software website

We need a multi page site with :

*What we do.
*How it works.
*Benefits
* Case study
* Testimonial
* Business login (we provide link to business portal)
* Consumer login (we provide link to consumer site)
* Book a demo
* Contact us

We want it to be clean and crisp and very self explanatory with little clutter. We are thinking white but are open to what ever looks the best.
Updates

Wordpress is preferred

Target Market(s)

Shopping centre managers and retail property companies

Coding

Coded - Design and coding required

Number of Pages Required

5+ page

Font styles to use
Sans Serif

Colors
ffffff

Requirements
Must have
• As listed above and must be responsive! Checkout our existing site for the text to be included (will be edited but it’ll give you an idea) www.tovrendix.com

```html
<!DOCTYPE html>
<html lang="en">
<head>
<meta charset="utf-8">
<title>Tovrendix – Shopping Centre Customer Engagement</title>
<link rel="stylesheet" href="https://fonts.googleapis.com/css2?family=Open+Sans:ital,wght@0,400;0,600;0,700;1,400&display=swap">
<style>
:root{
  --accent:#5cc6df;
  --accent-dark:#3fb3d0;
  --panel:#82cbe0;
  --panel-mid:#72c0d8;
  --footer:#83c7de;
  --ink:#2b2f33;
  --text:#6f7479;
  --muted:#9a9fa4;
  --soft-bg:#f6f7f9;
  --line:#e3e6e9;
  --white:#ffffff;
}
*{box-sizing:border-box;margin:0;padding:0}
html,body{width:1200px;height:3114px;overflow:hidden}
body{font-family:"Open Sans",Arial,sans-serif;color:var(--ink);background:var(--white);position:relative}
section,header,footer,nav{position:absolute;left:0;width:1200px}
.top-header{top:0;height:73px;border-top:4px solid var(--accent);background:var(--white)}
.brand{position:absolute;left:58px;top:12px;display:flex;align-items:center;gap:12px}
.brand-dot{width:44px;height:44px;border-radius:50%;background:#8d9398}
.brand-name{font-size:24px;font-weight:400;letter-spacing:3px;color:var(--ink)}
.main-nav{position:absolute;left:388px;top:27px;display:flex;gap:34px;font-size:13px;text-transform:uppercase;color:var(--ink)}
.login{position:absolute;top:18px;height:32px;border-radius:16px;font-size:13px;display:flex;align-items:center;justify-content:center}
.login-consumer{left:893px;width:133px;border:1.5px solid var(--accent);color:var(--accent)}
.login-business{left:1038px;width:125px;background:var(--accent);color:var(--white)}
.hero{top:73px;height:483px;background:linear-gradient(100deg,#6f6258 0%,#3d3a38 35%,#2f3034 60%,#5b5450 82%,#8a8580 100%)}
.hero-tag{position:absolute;left:282px;top:41px;width:254px;height:52px;background:var(--accent);color:var(--white);font-size:19px;font-weight:600;display:flex;align-items:center;justify-content:center}
.hero-tag::after{content:"";position:absolute;left:96px;bottom:-12px;border:12px solid transparent;border-bottom:0;border-top-color:var(--accent)}
.sub-nav{top:556px;height:36px;background:#ececec;font-size:11.5px;color:var(--muted)}
.sub-nav ul{position:absolute;left:52px;top:10px;display:flex;gap:22px;list-style:none}
.sub-nav li:first-child{color:#7d8287}
.social{position:absolute;top:9px;display:flex;gap:14px}
.social span{display:block;width:17px;height:17px;border-radius:3px}
.search{position:absolute;left:1132px;top:9px}
.intro{top:592px;height:151px;text-align:center}
.intro h1{position:absolute;top:13px;left:0;width:1200px;font-size:21px;font-weight:400;line-height:27px;color:var(--ink)}
.intro p{position:absolute;top:75px;left:0;width:1200px;font-size:13px;line-height:18px;color:var(--text)}
.btn-outline{display:inline-flex;align-items:center;justify-content:center;gap:8px;border-radius:18px;font-size:12px;font-weight:600;letter-spacing:1px;text-transform:uppercase}
.intro .btn-outline{position:absolute;left:525px;top:103px;width:150px;height:34px;border:1.5px solid var(--accent);color:var(--accent)}
.section-title{position:absolute;top:24px;left:0;width:1200px;text-align:center;font-size:22px;font-weight:700;color:var(--ink)}
.section-title em{font-style:normal;font-weight:400;color:var(--accent)}
.dotted{position:absolute;left:52px;width:1096px;border-top:1.5px dotted #b9dfea}
.process{top:743px;height:409px;background:var(--soft-bg)}
.process .dotted{top:67px}
.connector{position:absolute;top:170px;height:1px;background:#bfe3ee}
.step{position:absolute;top:128px;width:230px;text-align:center}
.step svg{display:block;margin:0 auto;height:84px}
.step h3{margin-top:28px;font-size:17px;font-weight:700}
.step p{margin-top:10px;font-size:12.5px;line-height:19px;color:var(--text)}
.highlights{top:1152px;height:391px;display:flex}
.highlight{width:400px;height:391px;background:var(--panel);color:var(--white);text-align:center;padding:28px 44px 0;position:relative}
.highlight.mid{background:var(--panel-mid)}
.highlight h2{font-size:24px;font-weight:700;line-height:32px}
.highlight p{margin-top:22px;font-size:12.5px;line-height:21px}
.highlight .btn-outline{position:absolute;left:50%;transform:translateX(-50%);top:316px;height:36px;padding:0 22px;border:1.5px solid var(--white);border-radius:3px;color:var(--white);white-space:nowrap}
.features{top:1543px;height:523px;background:var(--white)}
.features .dotted{top:69px}
.feature{position:absolute;width:274px;text-align:center}
.feature svg{display:block;margin:0 auto;height:56px}
.feature h3{margin-top:20px;font-size:16.5px;font-weight:700}
.feature p{margin-top:10px;font-size:12px;line-height:18px;color:var(--text);padding:0 4px}
.testimonials{top:2066px;height:405px;background:var(--soft-bg)}
.testimonials .dotted{top:62px}
.divider-v{position:absolute;left:600px;top:112px;height:245px;border-left:1.5px dotted #cfd4d8}
.divider-h{position:absolute;left:58px;top:232px;width:1090px;border-top:1.5px dotted #cfd4d8}
.quote{position:absolute;width:420px;font-size:11.5px;line-height:18px}
.quote blockquote{font-style:italic;color:var(--text)}
.quote cite{display:block;margin-top:6px;font-style:normal;color:var(--ink)}
.quote.left{left:58px;text-align:right}
.quote.right{left:737px;text-align:left}
.avatar{position:absolute;width:76px;height:76px;border-radius:50%;background:radial-gradient(circle at 50% 40%,#c9b4a6,#7d6a60)}
.stats{top:2471px;height:244px;background:var(--white)}
.stat{position:absolute;top:26px;width:253px;height:187px;color:var(--white);text-align:center}
.stat-bg{position:absolute;inset:0;background:linear-gradient(160deg,#4f5a66,#2a3038)}
.stat strong{position:relative;display:block;padding-top:44px;font-size:44px;font-weight:700}
.stat span{position:relative;display:block;margin-top:4px;font-size:17px;font-weight:600}
.site-footer{top:2715px;height:399px;background:var(--footer);color:var(--white)}
.footer-col{position:absolute;top:58px;font-size:11.5px;line-height:18px}
.footer-col h4{font-size:17px;font-weight:600;margin-bottom:16px}
.footer-col p{margin-bottom:14px}
.footer-col b{font-weight:700}
.footer-social{display:flex;gap:14px;margin-top:4px}
.footer-social span{width:12px;height:12px;border-radius:50%;background:var(--white)}
.footer-brand{position:absolute;left:842px;top:205px;width:280px;text-align:center;font-size:36px;font-weight:400;letter-spacing:5px;line-height:48px;color:#26333a}
.copyright{position:absolute;left:52px;top:326px;width:1096px;border-top:1px solid rgba(255,255,255,.6);text-align:center;padding-top:28px;font-size:11.5px}
</style>
</head>
<body>

<header class="top-header">
  <div class="brand"><span class="brand-dot"></span><span class="brand-name">TOVRENDIX</span></div>
  <nav class="main-nav"><span>How it works</span><span>Benefits</span><span>What we do</span><span>Case study</span></nav>
  <a class="login login-consumer">Consumer login</a>
  <a class="login login-business">Business login</a>
</header>

<section class="hero" role="img" aria-label="Photo of two young people in a café looking at their smartphones">
  <div class="hero-tag">Tovrendix.com/book-demo</div>
</section>

<nav class="sub-nav">
  <ul><li>Learn More:</li><li>Our Company</li><li>Testimonials</li><li>Careers</li><li>Help &amp; Contact</li></ul>
  <div class="social" style="left:996px">
    <span style="background:#3b5a9a"></span><span style="background:#3ea9dd"></span><span style="background:#d0533f"></span>
  </div>
  <svg class="search" width="16" height="16" viewBox="0 0 16 16"><circle cx="6.5" cy="6.5" r="4.5" fill="none" stroke="#8a8f94" stroke-width="2"/><line x1="10" y1="10" x2="14" y2="14" stroke="#8a8f94" stroke-width="2"/></svg>
</nav>

<section class="intro">
  <h1>Delight your shoppers, impress your tenants and provide your<br>landlords with accurate detailed data in real time</h1>
  <p>See some of the features below and learn why businesses trust Tovrendix</p>
  <a class="btn-outline">&#9654; Book a demo</a>
</section>

<section class="process">
  <h2 class="section-title">Our <em>Process</em></h2>
  <div class="dotted"></div>
  <div class="connector" style="left:205px;width:110px"></div>
  <div class="connector" style="left:440px;width:110px"></div>
  <div class="connector" style="left:650px;width:120px"></div>
  <div class="connector" style="left:885px;width:120px"></div>

  <div class="step" style="left:24px">
    <svg viewBox="0 0 84 84" fill="none" stroke="var(--accent)" stroke-width="2"><rect x="10" y="30" width="46" height="32" rx="4"/><line x1="10" y1="40" x2="56" y2="40"/><path d="M40 28l22-16 12 14-20 16"/></svg>
    <h3>Allocate Cards</h3>
    <p>Nemo enim ipsam voluptatem quia voluptas sit aspernatur aut odit aut fugit</p>
  </div>
  <div class="step" style="left:259px">
    <svg viewBox="0 0 84 84" fill="none" stroke="var(--accent)" stroke-width="2"><path d="M14 36h56l-7 30H21z"/><path d="M28 36c0-14 28-14 28 0"/><line x1="30" y1="44" x2="32" y2="60"/><line x1="42" y1="44" x2="42" y2="60"/><line x1="54" y1="44" x2="52" y2="60"/></svg>
    <h3>Direct Marketing</h3>
    <p>Nemo enim ipsam voluptatem quia voluptas sit aspernatur aut odit aut fugit</p>
  </div>
  <div class="step" style="left:481px">
    <svg viewBox="0 0 84 84" fill="none" stroke="var(--accent)" stroke-width="2"><rect x="30" y="8" width="24" height="44" rx="4"/><line x1="38" y1="46" x2="46" y2="46"/><path d="M28 40c-6 6-4 18 2 26h22c4-6 6-14 4-22"/></svg>
    <h3>Rewarding Loyalty</h3>
    <p>Nemo enim ipsam voluptatem quia voluptas sit aspernatur aut odit aut fugit</p>
  </div>
  <div class="step" style="left:711px">
    <svg viewBox="0 0 84 84" fill="none" stroke="var(--accent)" stroke-width="2"><path d="M12 28l40-12 18 26-40 14z"/><line x1="20" y1="38" x2="58" y2="26"/><circle cx="56" cy="58" r="10"/><line x1="56" y1="52" x2="56" y2="64"/><line x1="50" y1="58" x2="62" y2="58"/></svg>
    <h3>Collect Data</h3>
    <p>Nemo enim ipsam voluptatem quia voluptas sit aspernatur aut odit aut fugit</p>
  </div>
  <div class="step" style="left:946px">
    <svg viewBox="0 0 84 84" fill="none" stroke="var(--accent)" stroke-width="2"><path d="M64 30a26 26 0 1 1-10-10"/><path d="M50 14l6 8-8 5"/><circle cx="42" cy="42" r="14"/></svg>
    <h3>Data Analytics</h3>
    <p>Nemo enim ipsam voluptatem quia voluptas sit aspernatur aut odit aut fugit</p>
  </div>
</section>

<section class="highlights">
  <article class="highlight">
    <h2>Example Scenario</h2>
    <p>Tovrendix can predict more accurately and more reliably than ever before that on a cold wet Thursday next week: 35% of a retailers customers coming through their doors will be women aged between 30-35 looking to buy kids wear. When they arrive Tovrendix can identify them personally and send them messages based on where they are and their preferences.</p>
    <a class="btn-outline">Learn more</a>
  </article>
  <article class="highlight mid">
    <h2>Real Time Tracking</h2>
    <p>Tovrendix gives shopping centres real time tracking through smart ID's of individual customer journeys through their physical stores, enabling highly targeted, relevant and timely promotional and rewarding capabilities. Furthermore, through deep analytical data processing of the customer journey, centre managers will be able to more accurately and reliably predict shopping behaviours.</p>
    <a class="btn-outline">Learn on tracking</a>
  </article>
  <article class="highlight">
    <h2>Huge Benefits Potential</h2>
    <p>The potential benefits that Tovrendix offer shopping centres are huge. Tovrendix can enhance consumers' experience and simultaneously gather discrete, detailed location data that can be used to map shopping habits and staff activity. This insight will support the development of innovative centre layouts and customer service methods maximising</p>
    <a class="btn-outline">Learn on benefits</a>
  </article>
</section>

<section class="features">
  <h2 class="section-title">Our <em>Features</em></h2>
  <div class="dotted"></div>

  <div class="feature" style="left:52px;top:106px">
    <svg viewBox="0 0 56 56" fill="none" stroke="var(--accent)" stroke-width="2"><rect x="12" y="4" width="32" height="48"/><line x1="12" y1="16" x2="44" y2="16"/><line x1="18" y1="26" x2="38" y2="26"/><line x1="18" y1="34" x2="38" y2="34"/><line x1="18" y1="42" x2="30" y2="42"/></svg>
    <h3>Graphical Dashboard</h3><p>Sed ut perspiciatis unde omnis iste natus error sit voluptate accusantium doloremqu.</p>
  </div>
  <div class="feature" style="left:326px;top:106px">
    <svg viewBox="0 0 56 56" fill="none" stroke="var(--accent)" stroke-width="2"><rect x="4" y="6" width="48" height="44"/><line x1="4" y1="14" x2="52" y2="14"/><circle cx="28" cy="30" r="8"/><path d="M18 46c2-6 18-6 20 0"/></svg>
    <h3>Member Portal</h3><p>Nemo qui enim ipsam voluptatem quia voluptas sit aspernatur aut odit aut fugit.</p>
  </div>
  <div class="feature" style="left:600px;top:106px">
    <svg viewBox="0 0 56 56" fill="none" stroke="var(--accent)" stroke-width="2"><circle cx="28" cy="10" r="6"/><path d="M18 30c0-8 20-8 20 0v8H18z"/><line x1="28" y1="38" x2="28" y2="50"/><line x1="8" y1="50" x2="48" y2="50"/></svg>
    <h3>Lead Management</h3><p>Sed ut perspiciatis unde omnis iste natus error sit voluptatem accusantium quido et.</p>
  </div>
  <div class="feature" style="left:874px;top:106px">
    <svg viewBox="0 0 56 56"><circle cx="28" cy="28" r="24" fill="var(--accent)"/><circle cx="28" cy="28" r="8" fill="#fff"/><circle cx="16" cy="18" r="4" fill="#fff"/><circle cx="40" cy="18" r="4" fill="#fff"/><circle cx="28" cy="44" r="4" fill="#fff"/></svg>
    <h3>CRM</h3><p>Ut enim ad minim veniam, quis nostrud etor exercitation ullamco laboris nisi ut aliquipe.</p>
  </div>

  <div class="feature" style="left:52px;top:308px">
    <svg viewBox="0 0 56 56" fill="none" stroke="var(--accent)" stroke-width="2.5"><path d="M28 28c-6-10-22-10-22 0s16 10 22 0c6-10 22-10 22 0s-16 10-22 0z"/></svg>
    <h3>Billing Subscription</h3><p>Sed ut perspiciatis unde omnis iste natus error sit voluptate accusantium doloremqu.</p>
  </div>
  <div class="feature" style="left:326px;top:308px">
    <svg viewBox="0 0 56 56" fill="none" stroke="var(--accent)" stroke-width="2"><rect x="4" y="12" width="48" height="32" rx="3"/><rect x="10" y="20" width="14" height="8" fill="var(--accent)"/><line x1="10" y1="36" x2="44" y2="36"/></svg>
    <h3>Payment Gateway</h3><p>Nemo qui enim ipsam voluptatem quia voluptas sit aspernatur aut odit aut fugit.</p>
  </div>
  <div class="feature" style="left:600px;top:308px">
    <svg viewBox="0 0 56 56" fill="none" stroke="var(--accent)" stroke-width="2"><path d="M14 4h20l10 10v38H14z"/><path d="M34 4v10h10"/><rect x="18" y="34" width="22" height="12"/></svg>
    <h3>Invoicing</h3><p>Sed ut perspiciatis unde omnis iste natus error sit voluptatem accusantium quido et.</p>
  </div>
  <div class="feature" style="left:874px;top:308px">
    <svg viewBox="0 0 56 56" fill="none" stroke="var(--accent)" stroke-width="2"><path d="M28 4c8 8 8 24 4 34h-8c-4-10-4-26 4-34z"/><circle cx="28" cy="20" r="4"/><path d="M22 32l-6 8 8-2M34 32l6 8-8-2"/><line x1="28" y1="42" x2="28" y2="52"/></svg>
    <h3>Commission Tracking</h3><p>Duis aute irure dolor in reprehenderit in ter voluptate velit esse cillum dolore eu fugiat.</p>
  </div>
</section>

<section class="testimonials">
  <h2 class="section-title">What <em>People Say</em></h2>
  <div class="dotted"></div>
  <div class="divider-v"></div>
  <div class="divider-h"></div>

  <figure class="quote left" style="top:120px">
    <blockquote>Duis aute irure dolor in reprehenderit in voluptate velit esse cillum dolore eu fugiat nulla pariatur. Excepteur sint occaecat cupidatat non proident, sunt in culpa qui officia deserunt mollit.</blockquote>
    <cite>Evan Moretti, Operations Manager</cite>
  </figure>
  <div class="avatar" style="left:491px;top:132px" role="img" aria-label="Portrait photo of Evan Moretti"></div>
  <div class="avatar" style="left:630px;top:132px" role="img" aria-label="Portrait photo of Nora Halvey"></div>
  <figure class="quote right" style="top:120px">
    <blockquote>Provident, similique sunt in culpa qui officia deserunt mollitia animi, id est laborum et dolorum fuga. Et harum quidem rerum facilis est et expedita distinctio. Nam libero tempore, cum soluta nobis.</blockquote>
    <cite>Nora Halvey, Creative Designer</cite>
  </figure>

  <figure class="quote left" style="top:258px">
    <blockquote>Luis aute irure dolor in reprehenderit in pluptate velit esse cillum dolore eu fugiat nulla pariatur. Excepteur sint occaecat cupidatat non proident, sunt in culpa qui officia deserunt mollit.</blockquote>
    <cite>Greta Olsen, Manager</cite>
  </figure>
  <div class="avatar" style="left:491px;top:270px" role="img" aria-label="Portrait photo of Greta Olsen"></div>
  <div class="avatar" style="left:630px;top:270px" role="img" aria-label="Portrait photo of Ray Whitcombe"></div>
  <figure class="quote right" style="top:258px">
    <blockquote>At vero eos et accusamus et iusto odio dignissimos ducimus qui blanditiis praesentium voluptatum deleniti atque corrupti quos dolores et quas molestias excepturi sint occaecati asperiores.</blockquote>
    <cite>Ray Whitcombe, Developer</cite>
  </figure>
</section>

<section class="stats">
  <div class="stat" style="left:52px"><div class="stat-bg" role="img" aria-label="Photo of a shopper at a store counter"></div><strong>650</strong><span>VIP Card Holders</span></div>
  <div class="stat" style="left:332px"><div class="stat-bg" role="img" aria-label="Photo of people reading messages on phones"></div><strong>10500</strong><span>Messages Sent</span></div>
  <div class="stat" style="left:614px"><div class="stat-bg" role="img" aria-label="Photo of a shopping centre interior"></div><strong>980</strong><span>Loyalty Rewards Issued</span></div>
  <div class="stat" style="left:895px"><div class="stat-bg" role="img" aria-label="Photo of a busy retail store at night"></div><strong>95 %</strong><span>Tenant Engagement</span></div>
</section>

<footer class="site-footer">
  <div class="footer-col" style="left:52px;width:340px">
    <h4>Contact Us</h4>
    <p>Maecenas eros sit amet, consectetur adipiscing elit. Terminal volutpat rutrum metro amet sollicitudin interdum.</p>
    <p><b>Phone:</b> +1 (800) 555 0142</p>
    <p><b>Office:</b> Harbor Point Plaza</p>
    <p><b>Email:</b> contact@tovrendix.com</p>
    <div class="footer-social"><span></span><span></span><span></span><span></span><span></span></div>
  </div>
  <div class="footer-col" style="left:426px;width:370px">
    <h4>About Company</h4>
    <p>Enim congue blandit. Lorem ipsum dolor sit amet, consectetur adipiscing elit. Quisque consectetur interdum finibus. Vestibulum ante ipsum primis in faucibus orci, luctus et ultrices posuere.</p>
    <p>Cubilia cras blandit finibus ipsum, id porttitor arcu volutpat a. Integer iaculis est nec justo malesuada faucibus vel tempus sapien. Vivamus aliquam euismod tristique.</p>
  </div>
  <div class="footer-brand">TOVRENDIX</div>
  <div class="copyright">Copyright 2016. All Rights Reserved by Tovrendix</div>
</footer>

</body>
</html>
```